Wrenmoor Learning Houses MOXIE Poster

We need a poster to put up around our Community/Youth Centers that shows the acronym M.O.X.I.E. which stands for the traits our that make up the culture and personalities of our youth, families and staff. We would like the color scheme to be in our brand colors, and will send them as an upload (grey, blue, green). The poster must have our logo & tagline (uploaded), which may be small and not central. It should have the acronym with the associated words spelled out - as the smaller descriptive words as shown in uploaded attachment. It should be fun - youth friendly (ages 3-18) and really pop. I have also uploaded a sample poster that we created - but don't like....it feels boring, uninspired. It must say "The WLH" M.O.X.I.E as MOXIE is also the name of a different youth agency and we don't want our acronym to be confused with their name. Finally - to tell you a bit more about our organization I have uploaded our annual report. We can't way to see your ideas!!

Target Market(s)

Internal Information Poster for our community centers

Industry/Entity Type

Education

Font styles to use
Other font styles liked:
• FUN

Requirements
Must have
• It must say "The WLH" M.O.X.I.E as MOXIE is also the name of a different youth agency and we don't want our acronym to be confused with their name
• The WLH M.O.X.I.E. - and associated words - should be dominant/prevalent ....
Nice to have
• Fun Images/photos of actual sparks....
Should not have
• As described w/uploads

```html
<!DOCTYPE html>
<html lang="en">
<head>
<meta charset="utf-8">
<title>The WLH MOXIE Poster</title>
<link rel="stylesheet" href="https://fonts.googleapis.com/css2?family=Ultra&family=Open+Sans:wght@600;700&display=swap">
<style>
  :root {
    --teal: #56b8b5;
    --white: #ffffff;
    --grey: #77787b;
    --red: #d63f27;
    --yellow: #f3bd3d;
    --pink: #c868a8;
    --green: #7bb932;
    --aqua: #5dbfbb;
  }
  html, body {
    margin: 0;
    padding: 0;
    overflow: hidden;
    background: var(--white);
  }
  .poster {
    position: relative;
    width: 849px;
    height: 1200px;
    overflow: hidden;
    background: var(--white);
  }
  .band {
    position: absolute;
    left: 0;
    width: 100%;
    background: var(--teal);
  }
  .title {
    position: absolute;
    top: 6px;
    left: 0;
    width: 100%;
    margin: 0;
    text-align: center;
    font-family: "Ultra", "Rockwell Extra Bold", "Arial Black", serif;
    font-weight: 400;
    font-size: 118px;
    line-height: 150px;
    letter-spacing: 6px;
    color: var(--white);
  }
  .trait {
    position: absolute;
    left: 0;
    width: 100%;
    height: 160px;
  }
  .trait-badge {
    position: absolute;
    left: 62px;
    top: 0;
    width: 160px;
    height: 160px;
  }
  .trait-letter {
    font-family: "Ultra", "Rockwell Extra Bold", "Arial Black", serif;
    font-size: 112px;
    fill: var(--white);
  }
  .trait-word {
    position: absolute;
    left: 262px;
    top: 0;
    margin: 0;
    font-family: "Open Sans", sans-serif;
    font-weight: 700;
    font-size: 84px;
    line-height: 160px;
    letter-spacing: -1px;
    color: var(--grey);
  }
  .brand {
    position: absolute;
    left: 0;
    top: 1102px;
    width: 100%;
    text-align: center;
    font-family: "Open Sans", sans-serif;
  }
  .brand-name {
    margin: 0;
    font-weight: 700;
    font-size: 32px;
    line-height: 44px;
    letter-spacing: 1px;
    color: var(--grey);
    text-transform: uppercase;
  }
  .brand-tagline {
    margin: 4px 0 0;
    font-weight: 600;
    font-size: 20px;
    line-height: 28px;
    letter-spacing: 3px;
    color: var(--teal);
    text-transform: uppercase;
  }
</style>
</head>
<body>
<main class="poster">
  <div class="band" style="top:0;height:164px"></div>
  <div class="band" style="top:285px;height:71px"></div>
  <div class="band" style="top:477px;height:72px"></div>
  <div class="band" style="top:670px;height:71px"></div>
  <div class="band" style="top:862px;height:71px"></div>
  <div class="band" style="top:1047px;height:43px"></div>

  <h1 class="title">THE WLH</h1>

  <section class="trait" style="top:155px">
    <svg class="trait-badge" viewBox="0 0 160 160" aria-hidden="true">
      <circle cx="80" cy="80" r="78" fill="var(--red)"/>
      <text class="trait-letter" x="80" y="120" text-anchor="middle" transform="rotate(-6 80 80)">M</text>
    </svg>
    <p class="trait-word">INDFUL</p>
  </section>

  <section class="trait" style="top:340px">
    <svg class="trait-badge" viewBox="0 0 160 160" aria-hidden="true">
      <circle cx="80" cy="80" r="78" fill="var(--yellow)"/>
      <text class="trait-letter" x="80" y="120" text-anchor="middle" transform="rotate(-6 80 80)">O</text>
    </svg>
    <p class="trait-word">PTIMISTIC</p>
  </section>

  <section class="trait" style="top:518px">
    <svg class="trait-badge" viewBox="0 0 160 160" aria-hidden="true">
      <circle cx="80" cy="80" r="78" fill="var(--pink)"/>
      <text class="trait-letter" x="80" y="120" text-anchor="middle" transform="rotate(-6 80 80)">X</text>
    </svg>
    <p class="trait-word">PRESSIVE</p>
  </section>

  <section class="trait" style="top:704px">
    <svg class="trait-badge" viewBox="0 0 160 160" aria-hidden="true">
      <circle cx="80" cy="80" r="78" fill="var(--green)"/>
      <text class="trait-letter" x="80" y="120" text-anchor="middle" transform="rotate(-6 80 80)">I</text>
    </svg>
    <p class="trait-word">NCLUSIVE</p>
  </section>

  <section class="trait" style="top:903px">
    <svg class="trait-badge" viewBox="0 0 160 160" aria-hidden="true">
      <circle cx="80" cy="80" r="78" fill="var(--aqua)"/>
      <text class="trait-letter" x="80" y="120" text-anchor="middle" transform="rotate(-6 80 80)">E</text>
    </svg>
    <p class="trait-word">NERGETIC</p>
  </section>

  <footer class="brand">
    <p class="brand-name">Wrenmoor Learning Houses</p>
    <p class="brand-tagline">Room to grow together</p>
  </footer>
</main>
</body>
</html>
```